Clean, simple text based poster for printing: Street names using nice fonts

Clean/simple/typography: Street names poster

I am looking for a designer to make a simple text-based poster (A4/A3 size)

Basically, my parents have lived in many different places and I am looking for a poster which (a) shows all the streetnames they have lived in and (b) highlights in some way the last streetname, which is where they will retire.

- I am looking for clean/simple design with nice fonts.
- I had in mind perhaps different sizes and orientation of text.
- The streetnames should fill the whole canvas in a "tetris-like" fashion
- The "final" street name should stand out
- Perhaps a light background color, or a background image of some sort ...
- A light frame around the design

but then again, I'm a scientist and not a designer which is why I am here... so feel free to let the creative juices flow :)

The street names
- Corriston Road
- Brantwell Avenue
- Kolvaripur Street
- Kelbstraße
- Wurmelring
- Dunhollow Avenue
- Rue des Brumeliers
- Rue de Vostremont
- Pilzmayergasse
- Kromvigs Allé
- Lipečka Ulica
- Quernbachstraße
- Wolkenmarstraße
- Allée du Doux Crépuscule (Final street)

Ned

```html
<!DOCTYPE html>
<html lang="en">
<head>
<meta charset="utf-8">
<title>Street Names Poster</title>
<link rel="stylesheet" href="https://fonts.googleapis.com/css2?family=Saira+Condensed:wght@500&display=swap">
<style>
  :root {
    --page: #ffffff;
    --frame: #000000;
    --mat: #ffffff;
    --panel: #4a5775;
    --street: #9c9c9c;
    --final-street: #ffffff;
  }
  html, body {
    margin: 0;
    padding: 0;
    width: 865px;
    height: 1200px;
    overflow: hidden;
    background: var(--page);
  }
  .poster {
    position: relative;
    width: 865px;
    height: 1200px;
  }
  .frame {
    position: absolute;
    left: 29px;
    top: 29px;
    width: 803px;
    height: 1135px;
    background: var(--frame);
    box-shadow: 6px 8px 10px rgba(0, 0, 0, 0.35);
  }
  .mat {
    position: absolute;
    left: 62px;
    top: 62px;
    width: 736px;
    height: 1070px;
    background: var(--mat);
  }
  .panel {
    position: absolute;
    left: 133px;
    top: 126px;
    width: 604px;
    height: 958px;
    background: var(--panel);
    box-shadow: inset 0 0 6px rgba(0, 0, 0, 0.25);
  }
  .street-list {
    position: absolute;
    left: 0;
    top: 0;
    width: 865px;
    height: 1200px;
  }
  .street {
    font-family: "Saira Condensed", sans-serif;
    font-weight: 500;
    fill: var(--street);
  }
  .street--final {
    fill: var(--final-street);
  }
</style>
</head>
<body>
  <main class="poster">
    <div class="frame"></div>
    <div class="mat"></div>
    <div class="panel"></div>
    <svg class="street-list" viewBox="0 0 865 1200" aria-label="Streets lived on">
      <text class="street" x="166" y="226" font-size="80" textLength="538" lengthAdjust="spacingAndGlyphs">CORRISTON ROAD</text>
      <text class="street" x="166" y="278" font-size="62" textLength="538" lengthAdjust="spacingAndGlyphs">BRANTWELL AVENUE</text>
      <text class="street" x="166" y="330" font-size="62" textLength="538" lengthAdjust="spacingAndGlyphs">KOLVARIPUR STREET</text>
      <text class="street" x="166" y="423" font-size="120" textLength="538" lengthAdjust="spacingAndGlyphs">KELBSTRAßE</text>
      <text class="street" x="166" y="495" font-size="90" textLength="538" lengthAdjust="spacingAndGlyphs">WURMELRING</text>
      <text class="street" x="166" y="547" font-size="62" textLength="538" lengthAdjust="spacingAndGlyphs">DUNHOLLOW AVENUE</text>
      <text class="street" x="166" y="597" font-size="58" textLength="538" lengthAdjust="spacingAndGlyphs">RUE DES BRUMELIERS</text>
      <text class="street" x="166" y="649" font-size="62" textLength="538" lengthAdjust="spacingAndGlyphs">RUE DE VOSTREMONT</text>
      <text class="street" x="166" y="714" font-size="80" textLength="538" lengthAdjust="spacingAndGlyphs">PILZMAYERGASSE</text>
      <text class="street" x="166" y="789" font-size="74" textLength="538" lengthAdjust="spacingAndGlyphs">KROMVIGS ALLÉ</text>
      <text class="street" x="166" y="874" font-size="88" textLength="538" lengthAdjust="spacingAndGlyphs">LIPEČKA ULICA</text>
      <text class="street" x="166" y="929" font-size="66" textLength="538" lengthAdjust="spacingAndGlyphs">QUERNBACHSTRAßE</text>
      <text class="street" x="166" y="984" font-size="66" textLength="538" lengthAdjust="spacingAndGlyphs">WOLKENMARSTRAßE</text>
      <text class="street street--final" x="166" y="1042" font-size="50" textLength="538" lengthAdjust="spacingAndGlyphs">ALLÉE DU DOUX CRÉPUSCULE</text>
    </svg>
  </main>
</body>
</html>
```